Income Tax and Accounting Brochure

I need a brochure using my new logo (file attached). I do tax work and accounting work. I am an EA (QVX Enrolled Agent - logo attached) and would like this incorporated into the brochure. I also have a MSA in Accounting. Please incorporate the text that I have provided in the brochure.
Updates

Need extra days to review

Target Market(s)

Tax Clients - both business and individuals

Industry/Entity Type

Accounting

Colors
0054AA
0677BA
7BADD7
CADEEF
E8F1F8

Requirements
Must have
• Use my logo and the QVX EA file in the brochure
Nice to have
• I would like to see a brochure that I can customize with my own text if possible.

```html
<!DOCTYPE html>
<html lang="en">
<head>
<meta charset="utf-8">
<title>Harbor Ledger Accounting &amp; Consulting — Brochure</title>
<link rel="stylesheet" href="https://fonts.googleapis.com/css2?family=Montserrat:ital,wght@0,400;0,500;0,600;0,700;1,700&display=swap">
<style>
  :root{
    --red:#b01d2e;
    --red-deep:#7e1320;
    --blue:#0054aa;
    --blue-mid:#1f5bb5;
    --blue-light:#7badd7;
    --blue-pale:#cadeef;
    --blue-mist:#e8f1f8;
    --paper:#ffffff;
    --ink:#2b2f3a;
    --stage:#2a2a2a;
  }
  *{box-sizing:border-box;margin:0;padding:0}
  html,body{width:913px;height:1200px;overflow:hidden;background:var(--stage)}
  body{position:relative;font-family:"Montserrat",sans-serif;color:var(--ink)}
  .spread{position:absolute;left:20px;width:873px;height:560px;display:flex;box-shadow:0 10px 30px rgba(0,0,0,.5)}
  .spread--covers{top:20px}
  .spread--inside{top:620px}
  .page{position:relative;width:436.5px;height:560px;overflow:hidden;background:var(--paper)}
  .page>svg.page__art{position:absolute;inset:0;width:100%;height:100%}
  .fold{position:absolute;left:426px;top:0;width:21px;height:560px;background:linear-gradient(90deg,rgba(0,0,0,0),rgba(0,0,0,.12),rgba(0,0,0,0));pointer-events:none}

  /* back cover */
  .back__copy{position:absolute;left:28px;top:258px;width:340px;color:#fff}
  .back__headline{font-weight:700;font-size:18px;letter-spacing:.2px;white-space:nowrap;margin-bottom:8px}
  .back__intro{width:255px;font-size:8.3px;line-height:1.5}
  .contact{position:absolute;left:28px;top:412px;color:#fff}
  .contact__title{font-weight:600;font-size:16px;letter-spacing:.8px;margin-bottom:8px}
  .contact__row{display:flex;align-items:center;gap:8px;font-size:8.5px;letter-spacing:1px;margin-bottom:6px}
  .contact__icon{width:15px;height:15px;border-radius:4px;background:#fff;display:flex;align-items:center;justify-content:center}
  .contact__icon svg{width:10px;height:10px}

  /* front cover */
  .brand{position:absolute;right:26px;top:338px;width:170px;color:#fff;text-align:center;font-weight:600}
  .brand__mark{width:52px;height:52px;border-radius:50%;background:#fff;margin:0 auto 12px}
  .brand__name{font-size:14px;letter-spacing:1px;line-height:1.2}
  .brand__sub{font-size:9px;letter-spacing:2px;margin-top:3px}

  /* inside left */
  .about{position:absolute;left:30px;top:252px;width:380px}
  .about__title{width:300px;color:var(--red);font-weight:600;font-size:18px;line-height:1.15;margin-bottom:8px}
  .about__text{font-size:7.8px;line-height:1.5}
  .about__text p{margin-bottom:6px}
  .joy__title{color:var(--blue);font-weight:700;font-style:italic;font-size:13px;margin:6px 0 6px}
  .joy__text{width:370px;font-size:7.6px;line-height:1.5}
  .joy__text p{margin-bottom:6px}
  .joy__label{font-size:7px;color:#555}

  /* inside right */
  .benefits__title{position:absolute;left:34px;top:60px;color:var(--red);font-weight:600;font-size:19px}
  .benefits{position:absolute;left:24px;top:104px;width:385px;list-style:none}
  .benefits__item{display:flex;gap:12px;margin-bottom:12px;font-size:8.3px;line-height:1.5}
  .benefits__bullet{flex:none;width:22px;height:22px;border-radius:50%;background:var(--red);border:3px solid var(--blue-mid);display:flex;align-items:center;justify-content:center}
  .benefits__bullet svg{width:10px;height:10px}
</style>
</head>
<body>

<section class="spread spread--covers">
  <article class="page page--back">
    <svg class="page__art" viewBox="0 0 436.5 560" preserveAspectRatio="none">
      <defs>
        <linearGradient id="photoTop" x1="0" y1="0" x2="1" y2="1">
          <stop offset="0" stop-color="#dfe4ec"/><stop offset="1" stop-color="#9aa3b3"/>
        </linearGradient>
        <linearGradient id="redBody" x1="0" y1="0" x2="1" y2="1">
          <stop offset="0" stop-color="#b8202f"/><stop offset="1" stop-color="#7e1320"/>
        </linearGradient>
        <linearGradient id="photoDiag" x1="0" y1="0" x2="1" y2="1">
          <stop offset="0" stop-color="#c9ced8"/><stop offset="1" stop-color="#6f7a8e"/>
        </linearGradient>
      </defs>
      <rect role="img" aria-label="Photo of a hand using a calculator with a pen over financial papers" x="0" y="0" width="436.5" height="230" fill="url(#photoTop)"/>
      <path d="M0 150 C60 165 90 190 120 200 L0 215Z" fill="var(--blue-mid)"/>
      <path d="M0 205 C110 170 170 250 250 225 C330 200 380 140 436.5 120 L436.5 560 L0 560Z" fill="url(#redBody)"/>
      <path d="M0 198 C110 165 170 243 250 218 C330 193 380 133 436.5 113" fill="none" stroke="#e9b7a8" stroke-width="5"/>
      <path d="M130 238 C220 250 300 200 436.5 60" fill="none" stroke="var(--blue-mid)" stroke-width="1.5"/>
      <polygon role="img" aria-label="Photo of a desk with notebook, glasses and calculator" points="436.5,170 436.5,560 285,560" fill="url(#photoDiag)"/>
      <line x1="436.5" y1="165" x2="280" y2="560" stroke="#e25563" stroke-width="1.5"/>
    </svg>
    <div class="back__copy">
      <h2 class="back__headline">Books a Mess: No Problem!</h2>
      <p class="back__intro">If you own a small business and haven't kept up your bookkeeping, don't worry. We can help you. We'll prepare your bookkeeping for the year, prepare a full Schedule C, as well as your personal income tax return. Then we'll help you set up an easy system that allows you to keep your books in tip-top shape next year.</p>
    </div>
    <div class="contact">
      <h3 class="contact__title">CONTACT US</h3>
      <div class="contact__row"><span class="contact__icon"><svg viewBox="0 0 10 10"><path d="M2 1 L4 3 L3 4 C4 6 5 7 6 7 L7 6 L9 8 L8 9 C4 9 1 6 1 2Z" fill="var(--red)"/></svg></span>000 000 000 00</div>
      <div class="contact__row"><span class="contact__icon"><svg viewBox="0 0 10 10"><circle cx="5" cy="5" r="3.8" fill="none" stroke="var(--red)" stroke-width="1.2"/><path d="M1.2 5H8.8M5 1.2C3 3.5 3 6.5 5 8.8M5 1.2C7 3.5 7 6.5 5 8.8" fill="none" stroke="var(--red)" stroke-width=".8"/></svg></span>YOUR WEBSITE HERE</div>
      <div class="contact__row"><span class="contact__icon"><svg viewBox="0 0 10 10"><path d="M1 4.5 L9 1 L5.5 9 L4.5 5.5Z" fill="var(--red)"/></svg></span>ADDRESS,COUNTRY</div>
    </div>
  </article>

  <article class="page page--front">
    <svg class="page__art" viewBox="0 0 436.5 560" preserveAspectRatio="none">
      <defs>
        <linearGradient id="photoMeet" x1="0" y1="0" x2="1" y2="1">
          <stop offset="0" stop-color="#e6e9ef"/><stop offset="1" stop-color="#8c95a6"/>
        </linearGradient>
        <linearGradient id="photoDesk" x1="0" y1="0" x2="1" y2="1">
          <stop offset="0" stop-color="#f0ede6"/><stop offset="1" stop-color="#7e8aa0"/>
        </linearGradient>
      </defs>
      <rect x="0" y="0" width="436.5" height="560" fill="#f4f5f8"/>
      <rect x="36" y="34" width="70" height="34" fill="none" stroke="#6c8f8a" stroke-width="3"/>
      <rect x="42" y="40" width="58" height="22" fill="#e7e3d6"/>
      <rect role="img" aria-label="Photo of a team reviewing charts with a calculator on a table" x="150" y="28" width="210" height="175" rx="42" fill="url(#photoMeet)" stroke="var(--red)" stroke-width="7"/>
      <path d="M10 260 C120 200 200 250 300 230 C360 218 400 180 436.5 140" fill="none" stroke="var(--red)" stroke-width="1.6"/>
      <path d="M20 270 C130 212 210 262 310 242" fill="none" stroke="var(--red)" stroke-width="1"/>
      <path d="M120 40 C140 25 160 18 180 14" fill="none" stroke="var(--blue-mid)" stroke-width="1.2"/>
      <path d="M0 0 L35 0 L0 90Z" fill="#e9ebf0"/>
      <path role="img" aria-label="Photo of two people working over charts and documents with a pen" d="M0 300 C60 260 120 240 180 245 C240 250 290 260 300 330 L300 560 L0 560Z" fill="url(#photoDesk)"/>
      <path d="M436.5 160 C360 170 300 210 300 290 L300 340 C300 420 260 500 220 560 L436.5 560Z" fill="var(--blue-mid)"/>
    </svg>
    <div class="brand">
      <div class="brand__mark"></div>
      <div class="brand__name">HARBOR LEDGER ACCOUNTING</div>
      <div class="brand__sub">&amp; CONSULTING, LLC</div>
    </div>
  </article>
  <div class="fold"></div>
</section>

<section class="spread spread--inside">
  <article class="page page--about">
    <svg class="page__art" viewBox="0 0 436.5 560" preserveAspectRatio="none">
      <defs>
        <linearGradient id="photoCalc" x1="0" y1="0" x2="1" y2="1">
          <stop offset="0" stop-color="#eee6db"/><stop offset="1" stop-color="#a59a8e"/>
        </linearGradient>
      </defs>
      <rect width="436.5" height="560" fill="#f6f7f9"/>
      <path d="M70 0 L436.5 0 L436.5 160 C400 110 330 100 280 130 C230 160 170 180 140 140 C110 100 100 40 70 0Z" fill="var(--red)"/>
      <rect role="img" aria-label="Photo of hands on a calculator beside receipts" x="255" y="70" width="155" height="150" rx="34" transform="rotate(-8 332 145)" fill="url(#photoCalc)" stroke="var(--red)" stroke-width="2"/>
    </svg>
    <div class="about">
      <h2 class="about__title">About Maren T Caldwell, MSA EA (Principal)</h2>
      <div class="about__text">
        <p>I have a Masters' Degree in accounting and am an QVX Enrolled Agent. I am also a LedgerPro Advanced Certified Consultant in both the online and desktop products including Enterprise and Point of Sale. I provide individual and small business tax services, accounting, bookkeeping, QVX representation, insurance audit representation, business license assistance and more.</p>
        <p>I have experience working with a wide variety of clients from the point where they first decide they want to start a business. They are often unsure about what to do first. I have a lot of experience to offer you.</p>
      </div>
      <h3 class="joy__title">What a joy it is to watch success in action!</h3>
      <div class="joy__text">
        <p class="joy__label">Tax Preparation – why hire us?</p>
        <p>Preparing your own income tax return can be a task that leaves you with more questions than answers. According to a study released by the US National Audit Bureau last year, most taxpayers (77% of 71 million taxpayers) believe they benefited from using a professional tax preparer.</p>
        <p>Whether we like it or not, today's tax laws are so complicated that filing a relatively simple return can be confusing. It is just too easy to overlook deductions and credits to which you are entitled. Even if you use a computer software program there's no substitute for the assistance of an experienced tax professional.</p>
      </div>
    </div>
  </article>

  <article class="page page--benefits">
    <svg class="page__art" viewBox="0 0 436.5 560" preserveAspectRatio="none">
      <defs>
        <linearGradient id="photoCharts" x1="0" y1="0" x2="1" y2="1">
          <stop offset="0" stop-color="#d9dde4"/><stop offset="1" stop-color="#4b5260"/>
        </linearGradient>
      </defs>
      <rect width="436.5" height="560" fill="#f7f8fa"/>
      <path role="img" aria-label="Photo of a hand writing on printed charts beside a laptop" d="M0 440 C120 400 200 330 300 345 C370 355 410 400 436.5 440 L436.5 560 L0 560Z" fill="url(#photoCharts)"/>
      <path d="M0 436 C120 396 200 326 300 341 C370 351 410 396 436.5 436" fill="none" stroke="var(--blue-mid)" stroke-width="2"/>
    </svg>
    <h2 class="benefits__title">Here's what your get...</h2>
    <ul class="benefits">
      <li class="benefits__item"><span class="benefits__bullet"><svg viewBox="0 0 10 10"><path d="M2 5 L4 7 L8 3" fill="none" stroke="#fff" stroke-width="1.6"/></svg></span>Your tax return will be checked and rechecked by our computer software identifying potential problems the QVX may look at more closely and reviewing the math to limit QVX contacts.</li>
      <li class="benefits__item"><span class="benefits__bullet"><svg viewBox="0 0 10 10"><path d="M2 5 L4 7 L8 3" fill="none" stroke="#fff" stroke-width="1.6"/></svg></span>Your tax return can be filed electronically so you will get a refund back quicker.</li>
      <li class="benefits__item"><span class="benefits__bullet"><svg viewBox="0 0 10 10"><path d="M2 5 L4 7 L8 3" fill="none" stroke="#fff" stroke-width="1.6"/></svg></span>Our staff will show you how to adjust your payroll withholding to get more money back each week. Why give the QVX an interest free loan for up to 16 months.</li>
      <li class="benefits__item"><span class="benefits__bullet"><svg viewBox="0 0 10 10"><path d="M2 5 L4 7 L8 3" fill="none" stroke="#fff" stroke-width="1.6"/></svg></span>We will show you potential deductions to limit your tax liability for next year. In addition, we will give you a sheet of commonly overlooked deductions to limit the following year's tax liability.</li>
    </ul>
  </article>
  <div class="fold"></div>
</section>

</body>
</html>
```